Flyer-Design zum Animieren von Buchkäufen
Zielgruppe
Buchkäufer
Aufgabenstellung
Der Flyer soll zum Buchkauf animieren. Ausgelegt/verteilt wird er in Buchhandlungen, Museen, Ausstellungen.
Es handelt sich um ein geschichtswissenschaftliches Buch, der Flyer sollte diesen Charakter darstellen.

```html
<!DOCTYPE html>
<html lang="de">
<head>
<meta charset="utf-8">
<title>Flyer – Der Weiltinger Konflikt 1791/1792</title>
<link rel="stylesheet" href="https://fonts.googleapis.com/css2?family=Roboto+Condensed:wght@400;500&family=Oswald:wght@700&display=swap">
<style>
  :root{
    --sepia-dark:#9c5f22;
    --sepia-mid:#d58f45;
    --sepia-light:#f5c489;
    --paper:#ffffff;
    --ink:#1b1410;
    --ink-soft:#2a1d12;
    --headline:#fffaf2;
    --press-shade:#5a4330;
  }
  *{margin:0;padding:0;box-sizing:border-box}
  html,body{width:1200px;height:848px;overflow:hidden;background:var(--paper)}
  .spread{position:relative;width:1200px;height:848px;display:flex;font-family:"Roboto Condensed",sans-serif}

  .teaser{position:relative;width:607px;height:848px;overflow:hidden}
  .teaser-backdrop{
    position:absolute;inset:0;
    background:
      radial-gradient(ellipse 70% 35% at 20% 8%, rgba(120,70,25,.55), transparent 70%),
      radial-gradient(ellipse 60% 40% at 80% 30%, rgba(255,210,150,.55), transparent 70%),
      linear-gradient(180deg,var(--sepia-dark) 0%,var(--sepia-mid) 18%,var(--sepia-light) 40%,#f7cf9c 62%,#fbe7cf 82%,var(--paper) 100%);
  }
  .quote-mark{position:absolute;left:40px;top:40px;font-family:"Oswald",sans-serif;font-weight:700;font-size:92px;line-height:1;color:var(--paper)}
  .teaser-lead{
    position:absolute;left:30px;width:547px;top:123px;
    text-align:center;color:var(--headline);font-size:17.5px;line-height:29px;
    text-shadow:0 1px 4px rgba(70,35,5,.55);letter-spacing:-.2px
  }
  .highlights{position:absolute;left:40px;width:528px;top:243px;list-style:none;color:var(--ink-soft);font-size:15.2px;line-height:26px;letter-spacing:-.2px}
  .highlights li{position:relative;padding-left:17px;text-align:justify}
  .highlights li::before{content:"»";position:absolute;left:0;top:0}
  .press-clipping{
    position:absolute;left:76px;top:603px;width:455px;height:155px;
    background:linear-gradient(180deg,rgba(90,67,48,.28),rgba(90,67,48,.18));
    border-top:2px solid var(--ink);border-bottom:2px solid var(--ink);
  }

  .story{width:593px;padding:58px 28px 0 40px;color:var(--ink);font-size:12.6px;line-height:17.35px;letter-spacing:-.15px}
  .story p{text-align:justify;hyphens:auto;margin-bottom:17.35px}
</style>
</head>
<body>
<main class="spread">
  <section class="teaser">
    <div class="teaser-backdrop" role="img" aria-label="Sepiafarbene Collage aus historischer Landkarte der Wörnitzregion, Musketenläufen und Pulverdampf"></div>
    <div class="quote-mark">”</div>
    <p class="teaser-lead">Folgen Sie der literarischen Zeitreise in den Winter 1791/1792 und werden Sie Zeuge einer bewahrenswerten wirklich vorgefallenen Begebenheit, die mit allen Elementen einer spannenden Story gespickt ist.</p>
    <ul class="highlights">
      <li>ein politischer Skandal an einer uralten Grenze</li>
      <li>schicksalhaft für das Alte Reich</li>
      <li>systemsprengend</li>
      <li>ein Konflikt mit mehr als 400-jähriger Vorlaufzeit</li>
      <li>regionale Herrschaftsträger im Dauerkonflikt</li>
      <li>friedlich nicht mehr lösbar</li>
      <li>vielschichtig – von den Stuben der lokalen Bevölkerung bis in die Kabinette der Herrschenden</li>
      <li>ein Medienereignis im In- und Ausland</li>
    </ul>
    <div class="press-clipping" role="img" aria-label="Faksimile eines Zeitungskopfs in Frakturschrift vom 12. März 1792"></div>
  </section>

  <article class="story">
    <p>Mit dem Sturm auf die Bastille und der daraufolgenden Französischen Revolution im Jahr 1789 wurde der Grundstein zur Veränderung der Staats- und Gesellschaftssysteme in der westlichen Welt gelegt. In den Jahren danach waren die Reformer in Frankreich mit der Durchfechtung des neuen Gedankenguts beschäftigt, ehe sie zum Vorbild aller westlichen bürgerlichen Verfassungen wurde. Das neue Gedankengut in Europa führte zwischen 1792 und 1815 zu den Koalitions- und Revolutionskriegen, in deren Wechselwirkungen im vermeintlichen »Epochenjahr 1806« das Alte Reich erlosch. Doch nicht allein die großen Schlachten der »Schwellenzeit um 1800« und der territoriale Druck durch die siegreiche Revolutionstruppen konstatieren das Ende des Alten Reichs. Prägende Ereignisse, die im Rahmen der Arrondierungensbestrebungen der Nachfolger des Markgrafen von Ansbach und Bayreuth in den Jahren 1792 bis 1796 stattfanden, sollten für das Alte Reich zum »Point of no return« führen. Die Art und Weise wie Preußen versuchte, seine nachbarlichen Reichsritter, Reichsstädte und fremdherrlichen Unterthanen zu unterwerfen, beschädigten die Grundsätze der Alten Reichsverfassung irreversibel.</p>
    <p>Am 14. Februar 1792 entzündet sich im kleinen württembergischen Ort Weiltingen das erste Einzelstreichholz, das sich zu einem lokalen Großfeuer entwickelte und das die Gemüter im ganzen Reich erhitzte. Über den Vorfall hätten die beteiligten Regierungen am liebsten den Vorhang des Schweigens fallen lassen. Aufgewiegelte Nachbarn verübten aus Treue zur ihren Landesherrn unverhältnismässige »Thätlichkeiten« aneinander. Die größtenteils noch aus dem Mittelalter stammende Gesetzgebung war der umstrittenen und komplexen Herrschaftsituation am Hesselberg schonungslos ausgeliefert. Die alten Regeln und Gesetze konnten keine klärenden Antworten mehr auf den festgefahrenen jahrhundertalten Territorial- und Zuständigkeitszwist im wohl »strittigsten Dreieck« Deutschlands geben. Die aufgeheizte Situation an der Wörnitz war den kontradiktionären Umgebungsbedingungen nicht gewachsen, so dass im Sog des Weiltinger Konfikts Grundsatzfragen der alten Reichsverfassung zur Landeshoheit und zur exekutiven Rechtsausübung diskutiert werden mussten. Bei der Aufarbeitung der »farheuse afair de Wailtingen« prallten historische Ansichten und neues Gedankengut dermassen aneinander, dass an deren Reibfächen genügend Hitze für fundamentale politische Veränderungen entstand.</p>
    <p>Auf Basis von vielfachen neuen Erkenntnissen aus der jüngsten Geschichtsforschung und der Hinzuziehung umfangreicher historischer Quellen wird in diesem Buch der Frage nachgegangen, welcher Stellenwert den Weiltinger Geschehnisse in der Geschichte zugestanden werden kann? Waren die Ereignisse im Wörnitztal womöglich die ersten Axthiebe am alten Reichsstamm? Handelt es sich bei der Auseindersetzung gar um ein »tipping point-Ereignis«?</p>
    <p>Ausgehend von den drei lokalen Kernereignissen am Weiltinger Tor werden die Vorgänge in einem mehreren Ebenen umfassenden Gesamtkontext eingebunden. Dazu ist es nötig zum einen die Eigenheiten oder Besonderheiten der Antagonisten, der regionalen und lokalen Entwicklung, der lokalterritorialen Gegebenheiten und der Verhältnisse vor Ort zu beleuchten. Und zum andern muss der Blick auf die politische Großwetterlage gerichtet werden. Denn ohne die Verquickung der lokalen Verhältnisse mit zeitgenössischem Denken, althergebrachtem Rechtsverständnis und neuen politischen Strömungen wird man nicht verstehen, warum gerade die doch vielerorts gleichen Zutaten, sich ausgerechnet im Wörnitztal zu diesem explosiven Gebräu verbanden.</p>
  </article>
</main>
</body>
</html>
```